Banner ad for www.brightmoorly.example - Online Service for photographers

We need a simple and clean looking banner design that we can use in different formats and contexts online.

We're a new online service for photographers - providing websites, direct picture sales, media management, file delivery and cloud storage.

Our core message is 'Tools for Photographers': Sell Photos - Create Websites - Share Collections

Our target market is professional and 'serious amateur' photographers. We offer free 30 day trials. Members pay monthly or yearly subscriptions.

We're looking for something eye catching, graphically simple and modern that delivers the message clearly.

Required sizes are:

Leader board 728X90
Square pop up - 250x250
Wide skyscraper - 160x600
Button - 120x90

Target Market(s)

Our core target market is professional and serious amateur/enthusiast photographers.

Industry/Entity Type

Media

Requirements
Must have
• We need our logo

```html
<!DOCTYPE html>
<html lang="en">
<head>
<meta charset="utf-8">
<title>Brightmoorly – Tools for Photographers banner set</title>
<link rel="stylesheet" href="https://fonts.googleapis.com/css2?family=Montserrat:wght@400;600&display=swap">
<style>
  :root {
    --wood-light: #e2c9a0;
    --wood-mid: #d6ba8c;
    --wood-dark: #c9a878;
    --ink: #141414;
    --logo-ink: #3b3b3b;
    --stripe-yellow: #f9b81b;
    --stripe-orange: #f5841f;
    --stripe-red: #ee5423;
    --cta: #e8262b;
    --cta-text: #ffffff;
    --paper: #e9e8e4;
    --paper-shade: #b9b6ae;
    --canvas: #ffffff;
  }
  * { margin: 0; padding: 0; box-sizing: border-box; }
  html, body {
    width: 1200px; height: 1149px; overflow: hidden;
    background: var(--canvas);
    font-family: "Montserrat", Arial, sans-serif;
    color: var(--ink);
  }
  .canvas { position: relative; width: 1200px; height: 1149px; }

  .banner {
    position: absolute; overflow: hidden;
    background: linear-gradient(100deg, var(--wood-light) 0%, var(--wood-mid) 45%, var(--wood-light) 70%, var(--wood-dark) 100%);
  }
  .banner > * { position: absolute; }

  .brand { display: flex; align-items: center; font-weight: 600; color: var(--logo-ink); white-space: nowrap; line-height: 1; }
  .brand-mark { display: inline-block; flex: none; background: var(--logo-ink); margin-right: 0.3em; }

  .headline { font-weight: 400; text-align: center; line-height: 1.25; }
  .features { list-style: none; text-align: center; line-height: 1.22; font-weight: 400; }
  .cta {
    background: var(--cta); color: var(--cta-text); border-radius: 3px;
    display: flex; align-items: center; justify-content: center;
    font-weight: 400; white-space: nowrap;
    box-shadow: 0 1px 2px rgba(0,0,0,0.25);
  }
  .stripes { display: block; }
  .stripes .s1 { fill: var(--stripe-yellow); }
  .stripes .s2 { fill: var(--stripe-orange); }
  .stripes .s3 { fill: var(--stripe-red); }

  /* Square pop up */
  .banner-square { left: 55px; top: 75px; width: 393px; height: 390px; }
  .banner-square .brand { left: 26px; top: 86px; font-size: 24px; }
  .banner-square .brand-mark { width: 20px; height: 20px; }
  .banner-square .stripes { right: 0; top: 0; width: 150px; height: 150px; }
  .banner-square .headline { left: 0; right: 0; top: 152px; font-size: 44px; padding-left: 14px; }
  .banner-square .features { left: 20px; width: 200px; top: 292px; font-size: 18px; }
  .banner-square .cta { left: 246px; top: 304px; width: 120px; height: 55px; font-size: 17px; }

  /* Button */
  .banner-button { left: 55px; top: 512px; width: 187px; height: 140px; }
  .banner-button .brand { left: 14px; top: 38px; font-size: 12px; }
  .banner-button .brand-mark { width: 10px; height: 10px; }
  .banner-button .stripes { right: 0; top: 0; width: 62px; height: 62px; }
  .banner-button .headline { left: 0; right: 0; top: 66px; font-size: 14px; }
  .banner-button .features { left: 6px; width: 104px; top: 89px; font-size: 10px; line-height: 1.15; }
  .banner-button .cta { left: 117px; top: 101px; width: 55px; height: 24px; font-size: 8px; }

  /* Wide skyscraper */
  .banner-sky { left: 515px; top: 44px; width: 250px; height: 936px; }
  .banner-sky .stripes-top { left: 0; top: 0; width: 250px; height: 125px; }
  .banner-sky .brand { left: 0; right: 0; top: 172px; justify-content: center; font-size: 27px; }
  .banner-sky .brand-mark { width: 20px; height: 20px; }
  .banner-sky .stripes-mid { left: 0; top: 212px; width: 250px; height: 115px; }
  .banner-sky .headline { left: 0; right: 0; top: 341px; font-size: 31px; line-height: 1.3; }
  .banner-sky .features { left: 0; right: 0; top: 535px; font-size: 26px; line-height: 1.3; }
  .banner-sky .cta { left: 67px; top: 717px; width: 125px; height: 55px; font-size: 17px; }
  .banner-sky .notebook {
    left: 30px; top: 785px; width: 220px; height: 151px;
    background: linear-gradient(160deg, var(--paper) 0%, var(--paper) 60%, var(--paper-shade) 100%);
    transform: skewX(-6deg);
  }

  /* Leaderboard */
  .banner-leader { left: 55px; top: 994px; width: 1136px; height: 140px; }
  .banner-leader .brand { left: 36px; top: 92px; font-size: 28px; }
  .banner-leader .brand-mark { width: 22px; height: 22px; }
  .banner-leader .message { left: 237px; width: 560px; top: 16px; text-align: center; }
  .banner-leader .headline { position: static; font-size: 39px; line-height: 1.2; }
  .banner-leader .features { position: static; font-size: 22px; line-height: 1.3; }
  .banner-leader .cta { left: 810px; top: 37px; width: 145px; height: 64px; font-size: 21px; }
  .banner-leader .stripes { right: 0; top: 0; width: 161px; height: 140px; }
</style>
</head>
<body>
<main class="canvas">

  <section class="banner banner-square" aria-label="Square pop up banner">
    <svg class="stripes" viewBox="0 0 150 150" aria-hidden="true">
      <polygon class="s1" points="112,0 138,0 48,90 22,90"/>
      <polygon class="s2" points="150,10 150,38 60,128 32,128"/>
      <polygon class="s3" points="150,52 150,76 86,140 62,140"/>
    </svg>
    <div class="brand"><span class="brand-mark"></span>Brightmoorly</div>
    <h1 class="headline">Tools for<br>Photographers</h1>
    <ul class="features">
      <li>pictures sales</li>
      <li>personal websites</li>
      <li>file delivery</li>
      <li>cloud storage</li>
    </ul>
    <a class="cta">Try Us Free</a>
  </section>

  <section class="banner banner-button" aria-label="Button banner">
    <svg class="stripes" viewBox="0 0 150 150" aria-hidden="true">
      <polygon class="s1" points="112,0 138,0 48,90 22,90"/>
      <polygon class="s2" points="150,10 150,38 60,128 32,128"/>
      <polygon class="s3" points="150,52 150,76 86,140 62,140"/>
    </svg>
    <div class="brand"><span class="brand-mark"></span>Brightmoorly</div>
    <h2 class="headline">Tools for Photographers</h2>
    <ul class="features">
      <li>pictures sales</li>
      <li>personal websites</li>
      <li>file delivery</li>
      <li>cloud storage</li>
    </ul>
    <a class="cta">Try Us Free</a>
  </section>

  <section class="banner banner-sky" aria-label="Wide skyscraper banner">
    <svg class="stripes stripes-top" viewBox="0 0 250 125" aria-hidden="true">
      <polygon class="s1" points="40,0 90,0 10,80 0,80 0,40"/>
      <polygon class="s2" points="120,0 175,0 95,80 40,80"/>
      <polygon class="s3" points="200,0 250,0 250,10 180,80 125,80"/>
    </svg>
    <div class="brand"><span class="brand-mark"></span>Brightmoorly</div>
    <svg class="stripes stripes-mid" viewBox="0 0 250 115" aria-hidden="true">
      <polygon class="s3" points="0,0 60,0 0,60"/>
      <polygon class="s2" points="90,0 150,0 70,80 10,80"/>
      <polygon class="s1" points="190,0 250,0 250,20 155,115 95,115"/>
    </svg>
    <h2 class="headline">Tools<br>for<br>Photographers</h2>
    <ul class="features">
      <li>pictures sales</li>
      <li>personal websites</li>
      <li>file delivery</li>
      <li>cloud storage</li>
    </ul>
    <a class="cta">Try Us Free</a>
    <div class="notebook" role="img" aria-label="Photo of a spiral notebook page with a pen resting on it"></div>
  </section>

  <section class="banner banner-leader" aria-label="Leaderboard banner">
    <div class="brand"><span class="brand-mark"></span>Brightmoorly</div>
    <div class="message">
      <h2 class="headline">Tools for Photographers</h2>
      <ul class="features">
        <li>pictures sales - personal websites</li>
        <li>file delivery - cloud storage</li>
      </ul>
    </div>
    <a class="cta">Try Us Free</a>
    <svg class="stripes" viewBox="0 0 161 140" aria-hidden="true">
      <polygon class="s1" points="110,0 142,0 44,98 12,98"/>
      <polygon class="s2" points="161,14 161,46 67,140 35,140"/>
      <polygon class="s3" points="161,68 161,100 121,140 89,140"/>
    </svg>
  </section>

</main>
</body>
</html>
```